3 JPG Website Page Mockups need tidying / made into layered PSDs

Our website is aimed at creating a financial eduction site for females.

We have mockups of each page which are provided in jpeg.... but they need to be tidied up, layered into PSD (with descriptive layer names to allow coding from and no flattening - each object needs it's own layer) and we welcome any creative improvements suggested (although we are pretty happy with the way it's laid out at the moment as it is), without changing the feel, colour scheme or functionality of the site.

Three pages are needed:
Home page when not logged in
Home page when logged in
Topic header page

Please just upload the homepage to bid for the job... the winning designer will then have 5 days after they've been chosen to supply the psds of the other 2 pages .

I have also uploaded an image that can be used as a placeholder in the top box.
Thanks

As requested... Current font is Gill Sans MT

Thanks

Hi
Thanks for your designs.... For those of you still using the 4 circles (which I quite like), but haven't yet done so, could you see if you can move them around slightly to that the words don't get covered by the next circle?

Thanks

Reason: Designe has asked for An extension to work on new icons... would like to give them the time to see what they come up with, thanks

Industry/Entity Type

Financial

Requirements
Must have
• Maintain current feel & colour scheme of the website

```html
<!DOCTYPE html>
<html lang="en">
<head>
<meta charset="utf-8">
<title>The Money Sisterhood – Retirement</title>
<link href="https://fonts.googleapis.com/css2?family=Cabin:wght@400;500;600&family=Oswald:wght@400;500&family=Arimo:wght@400;700&display=swap" rel="stylesheet">
<style>
:root{
  --teal:#12a9b3;
  --teal-dark:#0c7f86;
  --teal-nav-top:#139aa0;
  --teal-nav-bottom:#0b7075;
  --orange:#e0441f;
  --orange-btn:#e2431c;
  --ink:#333333;
  --ink-soft:#444444;
  --header-bg:#e1e0e0;
  --body-bg:#efefef;
  --footer-bg:#e4e4e4;
  --line:#c9c9c9;
  --white:#ffffff;
}
*{box-sizing:border-box;margin:0;padding:0}
html,body{width:1200px;height:1097px;overflow:hidden;background:var(--body-bg)}
.page{position:relative;width:1000px;height:914px;transform:scale(1.2);transform-origin:0 0;font-family:"Cabin",sans-serif;color:var(--ink)}
.abs{position:absolute}

/* navigation */
.nav{left:0;top:0;width:1000px;height:45px;background:linear-gradient(var(--teal-nav-top),var(--teal-nav-bottom));border-bottom:1px solid #0a5d61}
.nav a{position:absolute;top:14px;color:var(--white);font-size:13px;text-decoration:none;font-family:"Arimo",sans-serif}
.nav .home{left:21px;top:7px;width:80px;height:30px;background:linear-gradient(#e9fdff,#8fe6ee);border-radius:4px;color:#0b5f66;text-align:center;line-height:30px;box-shadow:0 0 3px rgba(0,0,0,.3)}
.locale{left:913px;top:14px;color:var(--white);font-family:"Arimo",sans-serif;font-size:12px;display:flex;gap:8px;align-items:center}

/* header */
.header{left:0;top:45px;width:1000px;height:165px;background:var(--header-bg)}
.logo{left:20px;top:97px;font-family:"Arimo",sans-serif;font-size:40px;color:#222}
.prompt{left:348px;top:66px;font-family:"Oswald",sans-serif;font-size:19px;color:var(--orange);letter-spacing:.2px}
.search{left:348px;top:107px;width:315px;height:38px;background:var(--white);border:1px solid #cfcfcf;border-radius:19px;font-family:"Arimo",sans-serif;font-size:14px;color:#9a9a9a;padding:10px 0 0 17px}
.search svg{position:absolute;right:14px;top:8px}
.pill{height:38px;border-radius:19px;color:var(--white);font-family:"Arimo",sans-serif;font-size:13px;line-height:38px;padding-left:16px;box-shadow:0 1px 2px rgba(0,0,0,.25)}
.pill svg{position:absolute;right:10px;top:10px}
.pill.teal{background:var(--teal);color:#0d4f55}
.pill.orange{background:var(--orange-btn)}
.tabs{left:349px;top:167px;display:flex;align-items:center;font-size:14px;color:#333}
.tabs .on{background:#8b8b8b;color:var(--white);padding:2px 15px;border-radius:2px;margin-right:14px}
.tabs span+span{margin-right:28px}

/* sidebar */
.member-q{left:22px;top:239px;font-family:"Oswald",sans-serif;font-size:16px;color:var(--orange)}
.login{left:181px;top:226px;width:48px;height:48px;border-radius:50%;background:#333;color:var(--white);font-family:"Oswald",sans-serif;font-size:15px;text-align:center;line-height:48px}
.count{left:20px;top:289px;font-size:15px;color:#333}
.join{left:21px;top:328px;width:242px;height:43px;border-radius:22px;background:var(--orange-btn);color:var(--white);font-family:"Oswald",sans-serif;font-size:22px;line-height:43px;padding-left:18px}
.join svg{position:absolute;right:14px;top:9px}
.card{left:21px;width:204px;background:var(--white);border:1px solid var(--line);border-radius:4px}
.why{top:395px;height:137px;padding:12px 8px}
.why h3{font-family:"Oswald",sans-serif;font-weight:400;font-size:14px;color:#222;line-height:1.2}
.why h3 span{display:block;color:var(--orange);font-size:18px}
.why p{font-family:"Arimo",sans-serif;font-size:10.5px;line-height:1.35;margin-top:6px;color:#222}
.av{top:552px;height:198px;padding:10px 8px}
.av h3{font-family:"Oswald",sans-serif;font-weight:400;font-size:14px;color:#222}
.player{position:absolute;left:8px;top:40px;width:186px;height:146px;background:linear-gradient(#eceeef,#d9dcde);border:1px solid #d0d0d0}

.divider{left:277px;top:222px;width:1px;height:533px;background:var(--line)}

/* article */
.topic{left:293px;top:235px;font-family:"Oswald",sans-serif;font-size:21px;color:#333;display:flex;gap:12px;align-items:center}
.photo{left:293px;top:289px;width:238px;height:189px;border:1px solid #bbb;background:linear-gradient(135deg,#b9a58c 0%,#e8ddc9 40%,#8d7a63 75%,#5a4a3a 100%)}
.art-title{left:550px;top:287px;font-family:"Oswald",sans-serif;font-size:18px;color:var(--orange)}
.author{left:550px;top:322px;font-size:20px;color:var(--teal-dark);font-weight:500}
.role{left:550px;top:348px;font-size:11px;color:var(--teal-dark);font-weight:600}
.excerpt{left:550px;top:383px;width:380px;font-size:11.5px;line-height:1.55;color:var(--ink-soft)}
.more-cta{left:550px;top:473px;font-size:12px;color:var(--ink-soft)}
.more-cta b{color:var(--orange);font-weight:600}
.more-h{left:550px;top:488px;font-size:21px;color:#111}
.links{left:551px;top:529px;list-style:none;font-size:12px;line-height:18px;color:var(--ink-soft)}
.btn{top:629px;height:37px;border-radius:19px;font-family:"Arimo",sans-serif;font-size:13px;line-height:37px;padding-left:17px;box-shadow:0 1px 2px rgba(0,0,0,.25)}
.btn svg{position:absolute;right:10px;top:9px}
.tools{left:294px;top:701px;width:684px;height:29px;background:var(--white);border:1px solid var(--line);border-radius:4px;display:flex;align-items:center;padding-left:14px;gap:18px;font-family:"Arimo",sans-serif;font-weight:700;font-size:13px;color:#333}
.tools span{display:flex;align-items:center;gap:7px}

/* footer */
.footer{left:0;top:770px;width:1000px;height:144px;background:var(--footer-bg);border-top:2px solid #bdbdbd}
.sections{left:0;top:790px;width:1000px;display:flex}
.section{position:absolute;width:120px;text-align:center;font-family:"Arimo",sans-serif;font-weight:700;font-size:13px;color:#333}
.section i{display:block;margin:0 auto 10px;width:56px;height:60px;border-radius:10px}
</style>
</head>
<body>
<div class="page">

  <nav class="nav abs">
    <a class="home" href="#">Home</a>
    <a href="#" style="left:131px">Polls Events</a>
    <a href="#" style="left:247px">Learning Centre</a>
    <a href="#" style="left:388px">Find an Adviser</a>
    <a href="#" style="left:523px">Ask a Qestion</a>
    <a href="#" style="left:652px">About Us</a>
    <div class="locale abs">
      <svg width="20" height="13" viewBox="0 0 20 13"><rect width="20" height="13" fill="#1b2a7a"/><rect width="9" height="6" fill="#3355aa"/><path d="M0 3h9M4.5 0v6" stroke="#fff" stroke-width="1.4"/><path d="M0 3h9M4.5 0v6" stroke="#d22" stroke-width=".7"/><circle cx="15" cy="8" r="1" fill="#fff"/><circle cx="4.5" cy="10" r="1.2" fill="#fff"/></svg>
      AU
      <svg width="8" height="6" viewBox="0 0 8 6"><path d="M0 0h8L4 6z" fill="#fff"/></svg>
    </div>
  </nav>

  <header class="header abs"></header>
  <div class="logo abs">Company Logo</div>
  <div class="prompt abs">WHAT ARE YOU LOOKING FOR?</div>
  <div class="search abs">Search The Money Sisterhood for...
    <svg width="24" height="22" viewBox="0 0 24 22"><circle cx="9" cy="9" r="6.5" fill="none" stroke="var(--teal)" stroke-width="3"/><path d="M14 14l7 6" stroke="var(--teal)" stroke-width="4" stroke-linecap="round"/></svg>
  </div>
  <div class="pill teal abs" style="left:678px;top:107px;width:142px">Find an Adviser
    <svg width="18" height="18" viewBox="0 0 18 18"><circle cx="9" cy="9" r="9" fill="#fff"/><path d="M4.5 6.5h9L9 12.5z" fill="var(--teal)"/></svg>
  </div>
  <div class="pill orange abs" style="left:830px;top:107px;width:142px">Contact Us
    <svg width="18" height="18" viewBox="0 0 18 18"><circle cx="9" cy="9" r="9" fill="#fff"/><path d="M4.5 6.5h9L9 12.5z" fill="var(--orange)"/></svg>
  </div>
  <div class="tabs abs"><span class="on">Popular Searches</span><span>Explore the Learning Centre</span><span>Ask a Qestion</span></div>

  <aside>
    <div class="member-q abs">ALL READY A MEMBER?</div>
    <div class="login abs">LOGIN</div>
    <div class="count abs">288,426 Members and Growing</div>
    <div class="join abs">JOIN NOW FOR FREE
      <svg width="26" height="26" viewBox="0 0 26 26"><circle cx="13" cy="13" r="13" fill="#fff"/><path d="M6.5 9.5h13L13 18z" fill="var(--orange)"/></svg>
    </div>
    <div class="card why abs">
      <h3>WHY &nbsp;JOIN THE<span>MONEY SISTERHOOD</span></h3>
      <p>Discover all of the features available to members only, including interective tools, full articles and event participation.</p>
    </div>
    <div class="card av abs">
      <h3>AUDIO AND VIDEO</h3>
      <div class="player" role="img" aria-label="Audio and video player placeholder">
        <svg width="186" height="146" viewBox="0 0 186 146">
          <rect x="70" y="40" width="46" height="46" rx="3" fill="#333" opacity=".85"/>
          <path d="M86 52v22l18-11z" fill="#fff"/>
          <rect x="0" y="128" width="186" height="17" fill="#e8eaea" stroke="#bbb" stroke-width=".5"/>
          <path d="M6 132v8l6-4z" fill="#4a8a3a"/>
          <rect x="16" y="132" width="7" height="8" fill="#4a8a3a"/>
          <rect x="60" y="135" width="40" height="2" fill="#aaa"/>
        </svg>
      </div>
    </div>
  </aside>

  <div class="divider abs"></div>

  <main>
    <div class="topic abs">RETIREMENT
      <svg width="20" height="20" viewBox="0 0 20 20"><circle cx="10" cy="10" r="10" fill="var(--orange)"/><path d="M7.5 5.5v9l7-4.5z" fill="#fff"/></svg>
    </div>
    <div class="photo abs" role="img" aria-label="Photo of two women talking over coffee at a table"></div>
    <h2 class="art-title abs" style="font-weight:400">CREATING A RETIREMENT PLAN</h2>
    <div class="author abs">Kate Marlow</div>
    <div class="role abs">Adviser, Wealth Management, Sydney</div>
    <p class="excerpt abs">Women typically live 7 years longer than men, so wheather your retirement seems far off, or fast approching, knowing that you have a concrete paln in place to help you paln for retirement can make it that much easier...</p>
    <p class="more-cta abs">For the complete article <b>Login</b> or <b>Join Now... it's Free</b></p>
    <h2 class="more-h abs" style="font-weight:400">Looking for more information about Retirement</h2>
    <ul class="links abs">
      <li>Who needs a retirement plan?</li>
      <li>Investing in retirement</li>
      <li>So you're going to retire? A checklist for retirement</li>
      <li>how much do I need to retire on?</li>
    </ul>
    <div class="btn abs" style="left:547px;width:143px;background:var(--teal);color:#0d4f55">Find an Adviser
      <svg width="18" height="18" viewBox="0 0 18 18"><circle cx="9" cy="9" r="9" fill="#fff"/><path d="M4.5 6.5h9L9 12.5z" fill="var(--teal)"/></svg>
    </div>
    <div class="btn abs" style="left:707px;width:143px;background:var(--orange-btn);color:#fff">Ask a Question
      <svg width="18" height="18" viewBox="0 0 18 18"><circle cx="9" cy="9" r="9" fill="#fff"/><path d="M4.5 6.5h9L9 12.5z" fill="var(--orange)"/></svg>
    </div>
    <div class="tools abs">
      <span><svg width="18" height="18" viewBox="0 0 18 18"><circle cx="9" cy="9" r="9" fill="#333"/><path d="M7 5v8l6-4z" fill="#fff"/></svg>Add to bookmarks</span>
      <span><svg width="18" height="18" viewBox="0 0 18 18"><circle cx="9" cy="9" r="9" fill="#333"/><path d="M7 5v8l6-4z" fill="#fff"/></svg>Share</span>
      <span><svg width="18" height="18" viewBox="0 0 18 18"><circle cx="9" cy="9" r="9" fill="#333"/><path d="M7 5v8l6-4z" fill="#fff"/></svg>Email</span>
      <span><svg width="18" height="18" viewBox="0 0 18 18"><circle cx="9" cy="9" r="9" fill="#333"/><path d="M7 5v8l6-4z" fill="#fff"/></svg>Print</span>
    </div>
  </main>

  <footer class="footer abs"></footer>
  <div class="sections abs">
    <div class="section" style="left:16px"><i role="img" aria-label="Welcome icon" style="background:linear-gradient(#e0b48c,#6f8a96);border-radius:28px 28px 10px 10px"></i>Welcome</div>
    <div class="section" style="left:131px"><i role="img" aria-label="Events icon" style="width:46px;height:46px;margin-bottom:24px;background:#a3163f"></i>Events</div>
    <div class="section" style="left:247px"><i role="img" aria-label="Webcasts icon" style="width:54px;height:54px;border-radius:50%;background:radial-gradient(#d5d5d5,#777)"></i>Webcasts</div>
    <div class="section" style="left:366px"><i role="img" aria-label="My Family icon" style="background:linear-gradient(#d9261f 0 40%,#eeeeee 40%);border-radius:4px"></i>My Family</div>
    <div class="section" style="left:498px"><i role="img" aria-label="My Investments icon" style="background:linear-gradient(#ffffff,#e3e3e3);border:1px solid #ccc;border-radius:4px"></i>My Investments</div>
    <div class="section" style="left:609px"><i role="img" aria-label="My Retirement icon" style="width:58px;height:58px;border-radius:50%;background:radial-gradient(#e6f1ff,#2a6fc9)"></i>My Retirement</div>
    <div class="section" style="left:724px"><i role="img" aria-label="My Estate icon" style="background:linear-gradient(135deg,#1fb3c4,#b9ecf1);border-radius:6px"></i>My Estate</div>
    <div class="section" style="left:864px"><i role="img" aria-label="My Lifestyle icon" style="width:60px;height:60px;border-radius:50%;background:radial-gradient(#8fd36a,#2e8f1f)"></i>My Lifestyle</div>
  </div>

</div>
</body>
</html>
```